International Luxury Furniture and Accessories Outsourcing Company

We Need a Business Card design for a new Outsourcing company doing Business Internationally in the Luxury Furniture and Accessories Space. The company's name is MARCUS BELLWOOD and we deal with clients in the high end and Luxury Space for Furniture and Accessories in the world. We would like Designs that speaks Luxury and Professionalism.

We like the Combination of the color Brown and Gold or Black and Gold. We are also open to other color combo.

We like some of the design of file attached.
Updates

This is Peter and We really appreciate all of you taking the time out and putting the effort to help us jump start our new company. We have 2-3 designs that we like and will decide soon to pick one. Once again, Thank you to all of you !! Best Regards, Peter

Industry/Entity Type

Business

```html
<!DOCTYPE html>
<html lang="en">
<head>
<meta charset="utf-8">
<title>Marcus Bellwood – Business Card</title>
<link rel="stylesheet" href="https://fonts.googleapis.com/css2?family=Cinzel:wght@400;600&display=swap">
<style>
  :root {
    --page: #ffffff;
    --card: #f2f2f2;
    --card-edge: #c9c9c9;
    --ink: #111111;
    --gold: #e8a71e;
    --band: #e9aa1c;
  }
  * { margin: 0; padding: 0; box-sizing: border-box; }
  html, body {
    width: 989px;
    height: 1200px;
    overflow: hidden;
    background: var(--page);
  }
  body {
    position: relative;
    font-family: "Cinzel", "Times New Roman", serif;
    color: var(--ink);
  }
  .card {
    position: absolute;
    left: 101px;
    width: 797px;
    height: 513px;
    background: var(--card);
    border: 2px solid var(--card-edge);
    overflow: hidden;
  }
  .card--front { top: 68px; }
  .card--back { top: 626px; }

  /* front */
  .brand-mark {
    position: absolute;
    left: 50%;
    top: 118px;
    width: 150px;
    height: 150px;
    margin-left: -75px;
    border-radius: 50%;
    background: var(--gold);
  }
  .brand-name {
    position: absolute;
    left: 0;
    right: 0;
    top: 342px;
    text-align: center;
    font-size: 52px;
    font-weight: 400;
    letter-spacing: 2px;
    color: var(--ink);
  }

  /* back */
  .brand-name--small {
    position: absolute;
    left: 44px;
    top: 70px;
    font-size: 24px;
    font-weight: 400;
    letter-spacing: 1px;
    color: var(--ink);
  }
  .holder {
    position: absolute;
    right: 34px;
    top: 208px;
    text-align: right;
  }
  .holder__name {
    font-size: 62px;
    font-weight: 400;
    line-height: 1;
    letter-spacing: 1px;
    color: var(--ink);
  }
  .holder__title {
    margin-top: 12px;
    font-size: 42px;
    font-weight: 400;
    line-height: 1;
    letter-spacing: 2px;
    color: var(--gold);
  }
  .contact-band {
    position: absolute;
    left: 0;
    right: 0;
    bottom: 0;
    height: 77px;
    background: var(--band);
    display: flex;
    align-items: center;
    justify-content: space-between;
    padding: 0 30px 0 38px;
    font-size: 24px;
    font-weight: 600;
    color: var(--ink);
  }
  .contact-band__phone { font-variant: small-caps; }
</style>
</head>
<body>
  <section class="card card--front" aria-label="Card front">
    <div class="brand-mark" aria-hidden="true"></div>
    <h1 class="brand-name">MARCUS BELLWOOD</h1>
  </section>

  <section class="card card--back" aria-label="Card back">
    <div class="brand-name--small">MARCUS BELLWOOD</div>
    <div class="holder">
      <div class="holder__name">YOUR NAME</div>
      <div class="holder__title">JOB TITLE</div>
    </div>
    <div class="contact-band">
      <span class="contact-band__phone">Tel: 000-111-222</span>
      <span class="contact-band__web">WWW.[YOURWEBSITE].COM</span>
    </div>
  </section>
</body>
</html>
```